BRENSDALE ELECTRICAL

all black background with silver and lime writing, fonts i like are gothic style but am open to ideas, will need a picture logo aswell as im putting this on my van.i am a electrical contractor starting up my own electrical business. underneath brensdale electrical heading on card we could put" professiona cost effective soloutions to all your electrical needs".{ or something of that nature }.on aback of card on top half list servises provided, real estate and commercial maintenance, new home and renovation rewires and upgrades, split system air conditioning, floor heat, tv phone data, smoke detoctors, lighting systems , builders welcome, , and also a thankyou for your business.

Real Estate

GERALD PILWORTHY
brensdaleelectrical@mailvox.com.au
0417302951
lic no 58120
ac lic no l293417
abn 37216058814

```html
<!DOCTYPE html>
<html lang="en">
<head>
<meta charset="utf-8">
<title>Brensdale Electrical – Business Card</title>
<link rel="stylesheet" href="https://fonts.googleapis.com/css2?family=Archivo+Black&family=Questrial&family=Arimo&display=swap">
<style>
  :root {
    --card-black: #000000;
    --lime: #a9cc3c;
    --silver: #6d6e71;
    --icon-grey: #8a8b8e;
  }
  html, body {
    margin: 0;
    padding: 0;
    width: 1200px;
    height: 740px;
    overflow: hidden;
    background: var(--card-black);
  }
  .card {
    position: relative;
    width: 1200px;
    height: 740px;
    background: var(--card-black);
    overflow: hidden;
  }
  .credentials {
    position: absolute;
    top: 100px;
    right: 75px;
    margin: 0;
    text-align: right;
    font-family: "Questrial", sans-serif;
    font-size: 24px;
    line-height: 32px;
    letter-spacing: 0.5px;
    color: var(--lime);
  }
  .brand-mark {
    position: absolute;
    left: 560px;
    top: 140px;
    width: 80px;
    height: 80px;
    background: var(--lime);
  }
  .business-name {
    position: absolute;
    top: 286px;
    left: 0;
    width: 1200px;
    margin: 0;
    text-align: center;
    font-family: "Archivo Black", sans-serif;
    font-weight: 400;
    font-size: 50px;
    line-height: 60px;
    letter-spacing: 1px;
    color: var(--lime);
  }
  .tagline {
    position: absolute;
    top: 356px;
    left: 0;
    width: 1200px;
    margin: 0;
    text-align: center;
    font-family: "Arimo", sans-serif;
    font-size: 20px;
    color: var(--lime);
  }
  .contact {
    position: absolute;
    display: flex;
    align-items: center;
    font-family: "Questrial", sans-serif;
    font-size: 37px;
    color: var(--lime);
    letter-spacing: 0.5px;
  }
  .contact svg { fill: var(--icon-grey); flex: none; }
  .contact-phone { top: 552px; left: 452px; gap: 28px; }
  .contact-email { top: 610px; left: 272px; gap: 30px; }
</style>
</head>
<body>
  <main class="card">
    <p class="credentials">
      REC: 58120<br>
      AC LIC: L293417<br>
      ABN: 372 160 588 14
    </p>

    <div class="brand-mark" aria-hidden="true"></div>

    <h1 class="business-name">BRENSDALE ELECTRICAL</h1>
    <p class="tagline">The professional, efficient &amp; cost-effective solution for all your electrical needs</p>

    <div class="contact contact-phone">
      <svg width="18" height="34" viewBox="0 0 18 34" aria-hidden="true">
        <rect x="3" y="0" width="3" height="8"/>
        <rect x="1" y="7" width="16" height="27" rx="2"/>
        <rect x="4" y="10" width="10" height="7" fill="#000"/>
        <g fill="#000">
          <rect x="4" y="20" width="2" height="2"/><rect x="8" y="20" width="2" height="2"/><rect x="12" y="20" width="2" height="2"/>
          <rect x="4" y="24" width="2" height="2"/><rect x="8" y="24" width="2" height="2"/><rect x="12" y="24" width="2" height="2"/>
          <rect x="4" y="28" width="2" height="2"/><rect x="8" y="28" width="2" height="2"/><rect x="12" y="28" width="2" height="2"/>
        </g>
      </svg>
      <span class="phone-number">0417302951</span>
    </div>

    <div class="contact contact-email">
      <svg width="36" height="24" viewBox="0 0 36 24" aria-hidden="true">
        <rect x="0" y="0" width="36" height="24"/>
        <path d="M1 1 L18 14 L35 1" fill="none" stroke="#000" stroke-width="2"/>
        <path d="M1 23 L13 11 M35 23 L23 11" fill="none" stroke="#000" stroke-width="2"/>
      </svg>
      <span class="email-address">brensdaleelectrical@mailvox.com.au</span>
    </div>
  </main>
</body>
</html>
```